Business Card Design Project - Sports Brand

Lumora is a e-commerce fitness wear brand for ladies who are into gym, pole and swim.

Card should not be overly cluttered and should include the following:

1. logo
2. Name of the company (Use "Lumora Wear Pte Ltd" for now)
3. Address of company (Use a mock address)
4. Representative's name and contact info etc. (use a mock name and contact info)
5. website address

Target Market(s)

Women who are into pole , gym, and swim.

Women who shop online

Industry/Entity Type

E-Commerce

Colors

Designer to choose colors to be used in the design.

Requirements
Nice to have
• feminine sublimation of colours

Need not be printed on traditional paper. We would like the design to be revolutionary and interesting to the eye :)
Should not have
• the design should not be traditional looking. Do not include illustrations of Bikinis, yoga poses etc. in the card.

```html
<!DOCTYPE html>
<html lang="en">
<head>
<meta charset="utf-8">
<title>Lumora Wear – Business Card</title>
<link rel="stylesheet" href="https://fonts.googleapis.com/css2?family=Crimson+Text:ital,wght@0,400;0,700;1,400&display=swap">
<style>
  :root {
    --brand-red: #b8282f;
    --ink: #222222;
    --paper: #ffffff;
    --card-edge: #c9c9c9;
    --streak-light: rgba(255, 255, 255, 0.85);
    --streak-blush: rgba(232, 120, 150, 0.55);
    --text-font: "Crimson Text", Georgia, serif;
  }
  * { margin: 0; padding: 0; box-sizing: border-box; }
  html, body { width: 1200px; height: 852px; overflow: hidden; background: var(--paper); }
  .canvas { position: relative; width: 1200px; height: 852px; font-family: var(--text-font); }

  .card {
    position: absolute; left: 219px; top: 191px; width: 779px; height: 435px;
    border: 1.5px solid var(--card-edge); background: var(--paper); overflow: hidden;
  }
  .card__panel {
    position: absolute; left: 0; top: 0; width: 330px; height: 100%;
    background: var(--brand-red);
  }

  .company { position: absolute; right: 462px; top: 44px; text-align: right; color: var(--paper); }
  .company__name { font-size: 26px; font-weight: 700; line-height: 1.15; white-space: nowrap; }
  .company__tagline { font-size: 16px; line-height: 1.3; margin-right: -3px; }

  .brush-area {
    position: absolute; left: 150px; top: 118px; width: 178px; height: 186px;
    border-radius: 40% 8px 8px 40% / 50% 8px 8px 50%;
    background: linear-gradient(90deg, rgba(255,255,255,0) 0%, var(--streak-light) 55%, var(--streak-blush) 100%);
  }

  .brand-name {
    position: absolute; left: 346px; top: 178px;
    font-size: 72px; font-weight: 400; line-height: 1;
    color: var(--brand-red); white-space: nowrap;
  }

  .company-contact {
    position: absolute; right: 495px; top: 306px; text-align: right;
    color: var(--paper); font-size: 23px; line-height: 33px; white-space: nowrap;
  }

  .person { position: absolute; left: 499px; top: 42px; color: var(--ink); }
  .person__name { font-size: 34px; line-height: 1.2; }
  .person__role { font-size: 21px; font-style: italic; margin-top: 6px; letter-spacing: 0.5px; }

  .person-contact {
    position: absolute; left: 499px; top: 306px; color: var(--ink);
    font-size: 23px; line-height: 33px; white-space: nowrap;
  }
</style>
</head>
<body>
<div class="canvas">
  <div class="card">
    <div class="card__panel"></div>

    <div class="company">
      <p class="company__name">Lumora Wear Pte Ltd</p>
      <p class="company__tagline">Yoga · Swim · Pole</p>
    </div>

    <div class="brush-area" role="img" aria-label="Watercolour brush streak in white and blush pink leading into the brand name"></div>

    <p class="brand-name">Lumora</p>

    <div class="company-contact">
      <p>Address</p>
      <p>full address</p>
      <p>www.lumora.com</p>
    </div>

    <div class="person">
      <p class="person__name">Your Name</p>
      <p class="person__role">POSITION</p>
    </div>

    <div class="person-contact">
      <p>Phone number</p>
      <p>Fax</p>
      <p>Email:</p>
    </div>
  </div>
</div>
</body>
</html>
```